Business Card Design

I need a business card for my resume writing business. I have a logo that Im not keen on anymore so I would like the business card to use my photo instead of a logo. I am for mid career and trades resumes and prefer not to do executive resumes so don't need to aim for exectives. I would like it to be colourful. I like bright sky blue and maybe some pink or purple but primarily bright sky blue. I don't like green and Im keen see a fair bit of white on the card. As I have a photo to go it, it will need to go on a white background.

Target Market(s)

mid range careers. Not executives

Industry/Entity Type

Business

Contact Information for Business Card

Wyn Marchetti
Resume Writer
Clear Path CVs
27 The Lanyard
HARWOOD NSW 2465
wyn@clearpathcvs.com.au
0417362958
www.clearpathcvs.com.au

Requirements
Nice to have
• Maybe colours similar to my website - www.clearpathcvs.com.au but not with any black on it.
Should not have
• No green or dark colours

```html
<!DOCTYPE html>
<html lang="en">
<head>
<meta charset="utf-8">
<title>Wyn Marchetti – Resume Writer Business Card</title>
<link rel="stylesheet" href="https://fonts.googleapis.com/css2?family=Nunito:wght@700;800;900&family=Arimo:wght@400&display=swap">
<style>
  :root {
    --sky-light: #a9d3f5;
    --sky: #6fb2ea;
    --sky-deep: #4d97d8;
    --magenta: #e2259a;
    --magenta-deep: #c2187f;
    --violet-text: #55339a;
    --white: #ffffff;
    --page: #eef1f5;
    --photo-light: #f4f4f2;
    --photo-mid: #d9d6d2;
    --photo-warm: #b89683;
  }
  * { box-sizing: border-box; margin: 0; padding: 0; }
  html, body {
    width: 1200px;
    height: 900px;
    overflow: hidden;
    background: var(--page);
  }
  .business-card {
    position: absolute;
    left: 100px;
    top: 145px;
    width: 1000px;
    height: 610px;
    border-radius: 44px;
    overflow: hidden;
    background: var(--white);
    box-shadow: 0 10px 30px rgba(60, 90, 130, 0.18);
  }
  .sky-band {
    position: absolute;
    left: 0; top: 0;
    width: 100%;
    height: 260px;
    background: linear-gradient(180deg, var(--sky-light) 0%, var(--sky) 55%, var(--sky-deep) 100%);
  }
  .accent-stripe {
    position: absolute;
    left: 0;
    width: 100%;
    height: 10px;
    background: var(--magenta);
  }
  .accent-stripe.upper { top: 260px; }
  .accent-stripe.lower { top: 545px; height: 8px; }
  .base-band {
    position: absolute;
    left: 0; top: 553px;
    width: 100%;
    height: 57px;
    background: linear-gradient(180deg, var(--sky) 0%, var(--sky-deep) 100%);
  }
  .white-panel {
    position: absolute;
    left: 0; top: 270px;
    width: 100%;
    height: 275px;
    background: linear-gradient(180deg, #ffffff 0%, #ffffff 70%, #f1f3f6 100%);
  }
  .owner-name {
    position: absolute;
    left: 62px;
    top: 40px;
    font-family: "Nunito", sans-serif;
    font-weight: 800;
    font-size: 102px;
    line-height: 1;
    color: var(--magenta);
    letter-spacing: -1px;
  }
  .owner-role {
    position: absolute;
    left: 70px;
    top: 178px;
    font-family: "Nunito", sans-serif;
    font-weight: 800;
    font-size: 33px;
    line-height: 1;
    color: var(--white);
    letter-spacing: 0.52em;
  }
  .portrait {
    position: absolute;
    left: 650px;
    top: 165px;
    width: 290px;
    height: 380px;
    background: linear-gradient(180deg, var(--photo-warm) 0%, var(--photo-mid) 35%, var(--photo-light) 100%);
    border-radius: 120px 120px 0 0;
  }
  .contact-list {
    position: absolute;
    left: 42px;
    top: 292px;
    list-style: none;
    font-family: "Arimo", sans-serif;
    font-size: 33px;
    line-height: 40px;
    color: var(--violet-text);
  }
  .contact-item {
    display: flex;
    align-items: flex-start;
    margin-bottom: 6px;
  }
  .contact-icon {
    flex: none;
    width: 30px;
    height: 30px;
    margin: 5px 10px 0 0;
    fill: var(--magenta-deep);
  }
  .contact-text { display: block; }
</style>
</head>
<body>
  <main class="business-card">
    <div class="sky-band"></div>
    <div class="accent-stripe upper"></div>
    <div class="white-panel"></div>
    <div class="accent-stripe lower"></div>
    <div class="base-band"></div>

    <h1 class="owner-name">Wyn Marchetti</h1>
    <p class="owner-role">Resume Writer</p>

    <div class="portrait" role="img" aria-label="Portrait photo of Wyn Marchetti smiling, wearing a white jacket"></div>

    <ul class="contact-list">
      <li class="contact-item">
        <svg class="contact-icon" viewBox="0 0 24 24" aria-hidden="true">
          <path d="M6.6 10.8a15.1 15.1 0 0 0 6.6 6.6l2.2-2.2c.3-.3.7-.4 1-.2 1.1.4 2.3.6 3.6.6.6 0 1 .4 1 1V20c0 .6-.4 1-1 1C10.6 21 3 13.4 3 4c0-.6.4-1 1-1h3.5c.6 0 1 .4 1 1 0 1.2.2 2.4.6 3.6.1.3 0 .7-.2 1z"/>
        </svg>
        <span class="contact-text">0417362958</span>
      </li>
      <li class="contact-item">
        <svg class="contact-icon" viewBox="0 0 24 24" aria-hidden="true">
          <path d="M12 3 1.5 12H5v9h5.5v-6h3v6H19v-9h3.5z"/>
        </svg>
        <span class="contact-text">Clear Path CVs 27 The<br>Lanyard HARWOOD NSW 2465</span>
      </li>
      <li class="contact-item">
        <svg class="contact-icon" viewBox="0 0 24 24" aria-hidden="true">
          <path d="M2 8.5 12 2l10 6.5V20a1 1 0 0 1-1 1H3a1 1 0 0 1-1-1zm2 1.2 8 5.3 8-5.3L12 4.4z"/>
        </svg>
        <span class="contact-text">wyn@clearpathcvs.com.au</span>
      </li>
      <li class="contact-item">
        <svg class="contact-icon" viewBox="0 0 24 24" aria-hidden="true">
          <path d="M12 2a10 10 0 1 0 0 20 10 10 0 0 0 0-20zm6.9 6h-2.8a15 15 0 0 0-1.3-3.6A8 8 0 0 1 18.9 8zM12 4c.8 1.2 1.5 2.5 1.9 4h-3.8c.4-1.5 1.1-2.8 1.9-4zM4.3 14a8 8 0 0 1 0-4h3.3a16 16 0 0 0 0 4zm.8 2h2.8c.3 1.3.8 2.5 1.3 3.6A8 8 0 0 1 5.1 16zm2.8-8H5.1a8 8 0 0 1 4.1-3.6C8.7 5.5 8.2 6.7 7.9 8zM12 20c-.8-1.2-1.5-2.5-1.9-4h3.8c-.4 1.5-1.1 2.8-1.9 4zm2.3-6H9.7a14 14 0 0 1 0-4h4.6a14 14 0 0 1 0 4zm.5 5.6c.5-1.1 1-2.3 1.3-3.6h2.8a8 8 0 0 1-4.1 3.6zm1.6-5.6a16 16 0 0 0 0-4h3.3a8 8 0 0 1 0 4z"/>
        </svg>
        <span class="contact-text">www.clearpathcvs.com.au</span>
      </li>
    </ul>
  </main>
</body>
</html>
```